Website for Hargreave Fabrication & Construction Ltd

General Note to all.

1. Piling and gas works are separate areas of work and should not be put together.
- the marine section should really be the piling works and should have all the barges/water piles etc.
- the gas section should have the big silo looking thing

2. I would like to add in Specialist Onsite Labour and Management in the 'our services' section. The would include the Supervisors, Coded Welders, Site Fitters and Crane and Rig Crews etc.

3. I did like it how someone had use the HFC header logo as the top of the webpage with the individual tabs above and the website starting below. Please remove the VAT number and phone number from this section.

4. I also liked how one designer incorporate the orange line with spark (from the logo) as a page separator representing the welding part of the business

5. Add in a Mission Statement - To go above and beyond in to ensure our clients projects are delivered safely, ahead of schedule, in any environment for the benefit of not only our customers but also our employees and communities we work in.

6. Add in Business Objectives -HFC is on a mission to be one of the leading contractors in UK to supply All Site Labour - ranging from Site Management, fully Coded Welders, Site Fitters and Crane and Rig Crews.

7. I am happy for you to add in photos that are not ours for the thumbs nails for the our services. ie a colourful welding pics/cool tunnelling pic etc - just make sure I will not get done for copy write infringements

8. I would like a some type of 'contact us' field or 'request a consultation' section.

9. Please confirm if the webpages you create will be compatible for both desktop and mobile app and how difficult it will be to update personally once it is live.

10. You have all done very well and have thus far been very impressed with what you have produced. I gave a very vague brief as I was not entirely sure how you would go about making something with very little information. Some of the designs look very professional.

11. I'm not sure how once I choose the winning design how that then transfers over to my domain? Perhaps someone can help me with that? I will also be looking for a web hosting platform so feel free to provide this information.

After using Sketch hive for successful getting a professional logo for the company I'm giving the web design option a go.

I am looking for a professional website for the above civil construction company.

The company director has many years experience in Marine, tunnelling, conveyors, stadium construction gas and piling works including piling works for coal ports, bridges and tunnels.

The company currently provide 20+ skilled and experienced guys from all trades (supervisors, coded welders, fitters, crane drivers and crane supervisors, rigglers, slingers and piling operatives) on the Wenlow Causeway project in London - London's new super sewer. Most of this work is off barges carrying cranes (upto 600T and drill rigs).

As we are looking to expand and get more subcontracts we need a web presence to say who we are and what we do.

I'll include the 2 company logos we currently use below

I have included an info doc with pics you may or may not use.

Target Market(s)

Mainly other large construction companies and potential subcontractors

Industry/Entity Type

Construction Company

Coding

Coded - Design and coding required

Font styles to use
Sans Serif

Colors
0655a3
f37122
ffffff

Requirements
Must have
• Few tabs
• Simple to use/update but still professional look
• The challenge will be making the website look professional with not much available content.
Should not have
• No residential house building

```html
<!DOCTYPE html>
<html lang="en">
<head>
<meta charset="utf-8">
<title>Hargreave Fabrication &amp; Construction Ltd</title>
<link href="https://fonts.googleapis.com/css2?family=Montserrat:wght@400;500;600;700&family=Open+Sans:wght@400;600&display=swap" rel="stylesheet">
<style>
:root{
  --brand-blue:#0655a3;
  --brand-orange:#f37122;
  --navy:#15365c;
  --navy-band:#163457;
  --soft-blue:#9bbbd9;
  --page-grey:#f4f5f7;
  --footer-grey:#f3f3f3;
  --text-dark:#333c48;
  --text-muted:#7a8089;
  --white:#ffffff;
  --line:#e3e6ea;
}
*{box-sizing:border-box;margin:0;padding:0}
html,body{width:762px;height:1200px;overflow:hidden;background:var(--white)}
body{position:relative;font-family:"Open Sans",Arial,sans-serif;color:var(--text-dark)}
.abs{position:absolute}
.mont{font-family:"Montserrat",Arial,sans-serif}

/* header */
.site-header{left:0;top:0;width:762px;height:88px;background:var(--white);border-bottom:1px solid var(--line)}
.brand{left:97px;top:6px;display:flex;align-items:center;gap:6px}
.brand-mark{width:40px;height:40px;border-radius:50%;border:3px solid var(--brand-blue)}
.brand-name{font-family:"Montserrat",sans-serif;font-weight:700;font-size:26px;color:var(--brand-blue);letter-spacing:1px}
.top-icons{left:455px;top:13px;display:flex;gap:9px;align-items:center}
.top-icons .dot{width:8px;height:8px;border-radius:50%;background:#6b7280}
.call-us{left:540px;top:14px;font-family:"Montserrat",sans-serif;font-size:6px;font-weight:600;color:var(--brand-blue);letter-spacing:.4px}
.top-btn{top:29px;height:19px;border:1px solid #cfd4da;font-family:"Montserrat",sans-serif;font-size:6.5px;letter-spacing:.8px;font-weight:500;color:#555;display:flex;align-items:center;justify-content:center}
.nav-rule{left:0;top:64px;width:762px;height:1px;background:var(--line)}
.main-nav{left:110px;top:73px;display:flex;gap:21px;font-family:"Montserrat",sans-serif;font-size:6.5px;letter-spacing:.9px;font-weight:500;color:#555}
.main-nav .active{color:var(--brand-blue);font-weight:700}
.search{left:553px;top:69px;width:99px;height:16px;border:1px solid var(--brand-blue);display:flex}
.search span{flex:1;font-family:"Montserrat",sans-serif;font-size:6px;color:var(--brand-blue);padding:4px 5px;font-weight:600}
.search b{width:17px;background:var(--navy);display:flex;align-items:center;justify-content:center}

/* hero */
.hero{left:0;top:88px;width:762px;height:251px;background:linear-gradient(180deg,#5c6b7c 0%,#9a8a78 35%,#e8a24a 62%,#c36a1e 80%,#2a2a2c 100%)}
.hero-title{left:155px;top:201px;width:445px;height:39px;background:rgba(255,255,255,.32);display:flex;align-items:center;justify-content:center;font-family:"Montserrat",sans-serif;font-weight:600;font-size:21px;letter-spacing:2px;color:#2c2f36}

/* banner */
.project-band{left:0;top:339px;width:762px;height:48px;background:var(--navy-band)}
.project-text{left:109px;top:357px;font-family:"Montserrat",sans-serif;font-weight:700;font-size:8px;letter-spacing:.3px;color:var(--white)}
.project-text em{font-style:normal;color:var(--brand-orange)}
.chev{left:451px;top:355px}
.btn-orange{background:var(--brand-orange);color:var(--white);font-family:"Montserrat",sans-serif;font-weight:600;letter-spacing:1px;display:flex;align-items:center;justify-content:center}
.project-btn{left:470px;top:350px;width:182px;height:24px;font-size:8px}

/* feature cards */
.features{left:0;top:387px;width:762px;height:277px;background:var(--page-grey)}
.card{top:421px;width:161px;height:209px;background:var(--white);border:2px solid #e2e7ed}
.card .thumb{width:100%;height:87px}
.card h3{font-family:"Montserrat",sans-serif;font-weight:500;font-size:10.5px;letter-spacing:1.2px;color:#333;text-align:center;margin-top:12px}
.card p{font-size:6.5px;line-height:14.4px;letter-spacing:.6px;color:var(--text-muted);text-align:center;margin-top:5px}
.btn-soft{background:var(--soft-blue);color:var(--white);font-family:"Montserrat",sans-serif;font-weight:600;font-size:7.5px;letter-spacing:1px;display:flex;align-items:center;justify-content:center}
.card .btn-soft{width:89px;height:21px;margin:12px auto 0}

/* company + callback */
.company{left:0;top:664px;width:762px;height:209px;background:var(--navy)}
.section-head{font-family:"Montserrat",sans-serif;font-weight:700;font-size:11.5px;letter-spacing:1.3px;color:var(--brand-orange)}
.company-copy{left:110px;top:715px;width:227px;font-size:7.6px;line-height:14.4px;letter-spacing:.35px;color:var(--white);text-align:justify}
.more-btn{left:110px;top:816px;width:107px;height:21px}
.field{left:426px;width:226px;height:20px;border:1px solid var(--white);font-family:"Montserrat",sans-serif;font-size:8px;letter-spacing:.5px;color:var(--white);padding:4px 8px}
.callback-btn{left:426px;top:816px;width:88px;height:21px;font-size:7.5px;color:#15365c}

/* audience band */
.audience{left:0;top:873px;width:762px;height:110px;background:var(--brand-blue)}
.aud-item{top:890px;width:120px;text-align:center}
.aud-item svg{display:block;margin:0 auto}
.aud-item span{display:block;margin-top:7px;font-family:"Montserrat",sans-serif;font-weight:600;font-size:8.5px;line-height:13px;letter-spacing:1.1px;color:var(--white)}

/* footer */
.site-footer{left:0;top:983px;width:762px;height:182px;background:var(--footer-grey)}
.f-col{top:1017px;font-family:"Montserrat",sans-serif;font-size:6.5px;line-height:14.4px;letter-spacing:.4px;color:#555}
.f-col strong{font-weight:600;color:#333}
.f-input{left:408px;top:1054px;width:144px;height:20px;background:var(--white);border:1px solid #e4e4e4}
.subscribe{left:408px;top:1085px;width:78px;height:21px;background:var(--soft-blue);color:#2d4a6a}

/* partner strip */
.partners{left:0;top:1165px;width:762px;height:35px;background:var(--white);display:flex;justify-content:center;align-items:center;gap:22px}
.partners i{display:block;background:#c9ced6}
</style>
</head>
<body>

<header class="site-header abs">
  <div class="brand abs"><span class="brand-mark"></span><span class="brand-name">HFC</span></div>
  <div class="top-icons abs">
    <svg width="9" height="7" viewBox="0 0 9 7"><rect x=".5" y=".5" width="8" height="6" fill="none" stroke="#6b7280"/><path d="M.5 .5 4.5 4 8.5 .5" fill="none" stroke="#6b7280"/></svg>
    <span class="dot"></span><span class="dot"></span><span class="dot"></span>
  </div>
  <div class="call-us abs">CALL US NOW +44 (0)100 555 0199</div>
  <div class="top-btn abs" style="left:441px;width:107px">REQUEST A CALLBACK</div>
  <div class="top-btn abs" style="left:555px;width:97px">FIND A STOCKIST</div>
  <div class="nav-rule abs"></div>
  <nav class="main-nav abs">
    <span class="active">HOME</span><span>ABOUT US</span><span>SERVICES</span><span>PROJECTS</span><span>RESOURCES</span><span>CLIENTS</span><span>CONTACT</span>
  </nav>
  <div class="search abs"><span>SEARCH SITE</span><b><svg width="9" height="9" viewBox="0 0 9 9"><circle cx="5.2" cy="3.8" r="2.8" fill="none" stroke="#fff" stroke-width="1.2"/><path d="M3.2 5.8 .8 8.2" stroke="#fff" stroke-width="1.3"/></svg></b></div>
</header>

<div class="hero abs" role="img" aria-label="Photo of construction workers silhouetted on steel rebar at sunset"></div>
<h1 class="hero-title abs">EXPERTS IN CIVIL CONSTRUCTION</h1>

<section class="project-band abs"></section>
<p class="project-text abs">WE ARE PROUD TO BE WORKING ON THE <em>WENLOW CAUSEWAY</em> IN LONDON</p>
<svg class="chev abs" width="8" height="12" viewBox="0 0 8 12"><path d="M1.5 1 6.5 6 1.5 11" fill="none" stroke="#fff" stroke-width="1.6"/></svg>
<a class="project-btn abs btn-orange">VIEW PROJECT INFORMATION</a>

<section class="features abs"></section>
<article class="card abs" style="left:110px">
  <div class="thumb" role="img" aria-label="Photo of piling barges and cranes on the river" style="background:linear-gradient(180deg,#c9d0d8 0%,#aab3bd 55%,#6d7268 100%)"></div>
  <h3>OUR SERVICES</h3>
  <p>Lorem ipsum dolor sit ame tu<br>consectetur adipiscing elitone<br>uspen disse blandit placerat</p>
  <div class="btn-soft">READ MORE</div>
</article>
<article class="card abs" style="left:300px">
  <div class="thumb" role="img" aria-label="Map of south east England showing areas covered" style="background:linear-gradient(135deg,#e8eedc 0%,#cfe3c2 50%,#9fc9ee 100%)"></div>
  <h3>AREAS COVERED</h3>
  <p>Lorem ipsum dolor sit ame tu<br>consectetur adipiscing elitone<br>uspen disse blandit placerat</p>
  <div class="btn-soft">READ MORE</div>
</article>
<article class="card abs" style="left:491px">
  <div class="thumb" role="img" aria-label="Photo of a riverside construction site with cranes" style="background:linear-gradient(180deg,#b9c6d4 0%,#9aa6b0 55%,#6e6a62 100%)"></div>
  <h3>CASE STUDIES</h3>
  <p>Lorem ipsum dolor sit ame tu<br>consectetur adipiscing elitone<br>uspen disse blandit placerat</p>
  <div class="btn-soft">READ MORE</div>
</article>

<section class="company abs"></section>
<h2 class="section-head abs" style="left:110px;top:695px">OUR COMPANY</h2>
<p class="company-copy abs">Hargreave Fabrication &amp; Construction has over 15years experience working in the civil construction industry. We are currently working on the Wenlow Causeway project in London. We are subcontracted to Brantley Mercer Joint Venture and provide a highly skilled workforce across many of the Wenlow Causeway sites.</p>
<a class="more-btn abs btn-soft">MORE INFO</a>
<h2 class="section-head abs" style="left:426px;top:695px">REQUEST A CALL BACK</h2>
<div class="field abs" style="top:721px">Your Name</div>
<div class="field abs" style="top:752px">Phone Number</div>
<div class="field abs" style="top:782px">Email Address</div>
<a class="callback-btn abs btn-orange">CALL BACK</a>

<section class="audience abs"></section>
<div class="aud-item abs" style="left:117px">
  <svg width="46" height="46" viewBox="0 0 46 46"><circle cx="23" cy="23" r="21" fill="none" stroke="#fff" stroke-width="2.5"/><circle cx="17" cy="18" r="3.5" fill="#fff"/><circle cx="29" cy="18" r="3.5" fill="#fff"/><path d="M11 30c0-5 3-7 6-7s6 2 6 7zM23 30c0-5 3-7 6-7s6 2 6 7z" fill="#fff"/></svg>
  <span>END USER<br>INFORMATION</span>
</div>
<div class="aud-item abs" style="left:253px">
  <svg width="46" height="46" viewBox="0 0 46 46"><circle cx="23" cy="23" r="21" fill="none" stroke="#fff" stroke-width="2.5"/><path d="M13 25h18M16 25v9M28 25v9" stroke="#fff" stroke-width="2"/><circle cx="27" cy="15" r="3" fill="#fff"/><path d="M24 24l2-6h3l1 6z" fill="#fff"/></svg>
  <span>SPECIFIER<br>INFORMATION</span>
</div>
<div class="aud-item abs" style="left:388px">
  <svg width="46" height="46" viewBox="0 0 46 46"><circle cx="23" cy="23" r="21" fill="none" stroke="#fff" stroke-width="2.5"/><path d="M16 18a7 6 0 0 1 14 0z" fill="#fff"/><circle cx="23" cy="21" r="4" fill="#fff"/><path d="M14 34c0-6 4-8 9-8s9 2 9 8z" fill="#fff"/></svg>
  <span>CONTRACTOR<br>INFORMATION</span>
</div>
<div class="aud-item abs" style="left:524px">
  <svg width="46" height="46" viewBox="0 0 46 46"><circle cx="23" cy="23" r="21" fill="none" stroke="#fff" stroke-width="2.5"/><path d="M12 27v-8h6l3 4v4z" fill="#fff"/><rect x="23" y="17" width="5" height="10" fill="#fff"/><rect x="29" y="20" width="5" height="7" fill="#fff"/><circle cx="15" cy="29" r="2" fill="#fff"/></svg>
  <span>DISTRIBUTOR<br>INFORMATION</span>
</div>

<footer class="site-footer abs"></footer>
<div class="f-col abs" style="left:110px">© Copyright 2018<br>Hargreave Fabrication &amp; Construction<br>8 Ashcombe Lane<br>Fenbury<br>Surrey<br>FB2 7QL</div>
<div class="f-col abs" style="left:252px"><strong>Contact Info</strong><br>Telephone: +44 (0)100 555 0142<br>Fax: 0100 555 0143<br>Email: info@hargreavefc.example</div>
<div class="f-col abs" style="left:408px"><strong>Join our Mailing List</strong><br><span style="color:#888">Enter your email below:</span></div>
<div class="f-input abs"></div>
<a class="subscribe abs btn-soft">SUBSCRIBE</a>
<div class="f-col abs" style="left:584px;color:#333;font-weight:500">About Us<br>Services<br>Projects<br>Resources<br>Case Studies<br>Contact Us<br>Terms &amp; Conditions<br>Privacy Policy</div>

<div class="partners abs">
  <i style="width:18px;height:22px"></i>
  <i style="width:26px;height:22px"></i>
  <i style="width:30px;height:22px;border-radius:50%"></i>
  <i style="width:40px;height:16px"></i>
  <i style="width:44px;height:20px"></i>
</div>

</body>
</html>
```